Harlow Pennick Group Business Cards

We have a new logo, and want to design new business cards with it. We are 21 years in business, and want a fresh but professional look, so not a lot of extra stuff on the card. We are a recruiting and staffing firm focused on placing accounting and finance professionals in the Dallas TX area. I've attached our new logo that should be displayed on the cards. Here is what I think we want on the cards:
Ned Varcombe, CPA
Partner and Managing Director
8262 Quarry Mill Rd.
Suite 610
Dallas, TX 75391
O 214-583-9071
M 214-690-1482
ned@harlowpennick-example.com
www.harlowpennick-example.com

```html
<!DOCTYPE html>
<html lang="en">
<head>
<meta charset="utf-8">
<title>Harlow Pennick Group – Business Cards</title>
<link href="https://fonts.googleapis.com/css2?family=Montserrat:wght@400;600&display=swap" rel="stylesheet">
<style>
  :root {
    --backdrop: #2e2e2e;
    --card-white: #ffffff;
    --brand-blue: #23409a;
    --card-blue: #233f94;
    --mark-on-blue: #2d4ba6;
    --ink: #2b2b2b;
  }
  * { margin: 0; padding: 0; box-sizing: border-box; }
  html, body {
    width: 1200px; height: 897px; overflow: hidden;
    background: var(--backdrop);
    font-family: "Montserrat", sans-serif;
  }
  .canvas { position: relative; width: 1200px; height: 897px; }
  .card {
    position: absolute; left: 303px; width: 595px; height: 338px; overflow: hidden;
  }
  .card--front { top: 92px; background: var(--card-white); color: var(--ink); }
  .card--back { top: 469px; background: var(--card-blue); }

  .brand-name {
    position: absolute; left: 39px; top: 40px; width: 204px;
    text-align: center; color: var(--brand-blue);
    font-weight: 600; font-size: 20px; line-height: 1.25; letter-spacing: 0.2px;
    text-transform: uppercase;
  }
  .person { position: absolute; left: 326px; top: 68px; }
  .person__name { color: var(--brand-blue); font-weight: 600; font-size: 20px; letter-spacing: 0.2px; line-height: 1.2; white-space: nowrap; }
  .person__title { font-size: 14px; line-height: 1.3; margin-top: 2px; }

  .contact { position: absolute; left: 327px; top: 156px; list-style: none; font-size: 13px; }
  .contact li { display: flex; align-items: center; height: 20px; white-space: nowrap; }
  .contact svg { width: 11px; height: 11px; margin-right: 8px; flex: none; }

  .address { position: absolute; left: 326px; top: 269px; font-size: 14px; line-height: 1.4; font-style: normal; }
  .website { position: absolute; left: 39px; top: 289px; font-size: 14px; white-space: nowrap; }
  .website__domain { color: var(--brand-blue); }

  .brand-name--back {
    position: absolute; left: 0; right: 0; top: 128px;
    text-align: center; color: var(--mark-on-blue);
    font-weight: 600; font-size: 34px; line-height: 1.2; text-transform: uppercase;
  }
</style>
</head>
<body>
<main class="canvas">
  <section class="card card--front">
    <div class="brand-name">Harlow Pennick<br>Group</div>

    <div class="person">
      <div class="person__name">NED VARCOMBE, CPA</div>
      <div class="person__title">Partner and Managing Director</div>
    </div>

    <ul class="contact">
      <li>
        <svg viewBox="0 0 12 12" aria-hidden="true"><path d="M3 1 L5 3.5 L4 5 Q5.5 7.5 7.5 8.5 L9 7.5 L11 9.5 L9.5 11 Q4 10 1.5 3 Z" fill="none" stroke="var(--brand-blue)" stroke-width="1.2"/></svg>
        214-583-9071
      </li>
      <li>
        <svg viewBox="0 0 12 12" aria-hidden="true"><rect x="3" y="0.8" width="6" height="10.4" rx="1" fill="none" stroke="var(--brand-blue)" stroke-width="1.3"/><circle cx="6" cy="9" r="0.8" fill="var(--brand-blue)"/></svg>
        214-690-1482
      </li>
      <li>
        <svg viewBox="0 0 12 12" aria-hidden="true"><rect x="0.8" y="2.5" width="10.4" height="7" fill="none" stroke="var(--brand-blue)" stroke-width="1.2"/><path d="M1 3 L6 6.5 L11 3" fill="none" stroke="var(--brand-blue)" stroke-width="1.2"/></svg>
        ned@harlowpennick-example.com
      </li>
    </ul>

    <address class="address">8262 Quarry Mill Rd. Suite<br>610 Dallas, TX 75391</address>

    <div class="website">www.<span class="website__domain">harlowpennick-example</span>.com</div>
  </section>

  <section class="card card--back">
    <div class="brand-name--back">Harlow Pennick<br>Group</div>
  </section>
</main>
</body>
</html>
```